Create a business Card for a Women Owned Business Body Positive Company. The winner we hope to work with on other projects coming up for grand opening for flyers, postcards, email marketing, facebook page, stationary, labels, tshirt design....
We would like if possible in the background of the card a infinity symbol or crown if it fits into the design if not it's ok. But I am open to all suggestions we had alot problems with the our new logo being created this time sad to say :(

Our colors are Royal Purple, Grey, Black Thank you in advance for your talent, you hard work and your submissions!
Delia and Harriet :)

my Logo is lantern meadow boutique which is purple and has a heart and infinity sign in it and my colors are purple silver and black only of another card i had done nothing else. My logo is LANTERN MEADOW BOUTIQUE LOGO

Industry/Entity Type

Retail

Contact Information for Business Card

website: www.lantrnmeadowboutiques.example email: sales@lanternmeadowboutique.example
Delia Rookwell & Harriet Quinlan Owners

Font styles to use
Script

Colors
b768aa

Requirements
Must have
• COLORS ARE PURPLE BLACK AND GREY
Nice to have
• INFINITY SIGNING IN THE BACKGROUND

```html
<!DOCTYPE html>
<html lang="en">
<head>
<meta charset="utf-8">
<title>Lantern Meadow Boutique – Business Card</title>
<link rel="stylesheet" href="https://fonts.googleapis.com/css2?family=Cinzel:wght@400;600&family=PT+Serif&display=swap">
<style>
  :root {
    --bg: #1c1c1e;
    --purple: #744a9e;
    --grey: #d2d1d3;
    --silver: #e4e4e6;
    --black: #050505;
    --white: #f6f4f8;
    --ink: #1a1a1a;
  }
  * { box-sizing: border-box; margin: 0; padding: 0; }
  html, body { width: 1200px; height: 1200px; overflow: hidden; }
  body {
    background: var(--bg);
    display: flex;
    flex-direction: column;
    align-items: center;
    justify-content: center;
    gap: 70px;
  }
  .card {
    position: relative;
    width: 860px;
    height: 491px;
    background: var(--black);
    overflow: hidden;
    box-shadow: 0 14px 40px rgba(0,0,0,.55);
  }
  .card__accent {
    position: absolute;
    inset: 0;
    clip-path: polygon(44% 0, 100% 0, 100% 100%, 64% 100%);
  }
  .card--front .card__accent { background: var(--silver); }
  .card--back .card__accent { background: var(--purple); clip-path: polygon(58% 0, 100% 0, 100% 100%, 74% 100%); }
  .card__panel {
    position: absolute;
    top: 14px; left: 16px; right: 22px; bottom: 16px;
  }
  .card--front .card__panel { background: var(--purple); }
  .card--back .card__panel {
    background: linear-gradient(135deg, #c9c8ca 0%, #dedddf 55%, #cfced0 100%);
  }

  .brand {
    font-family: "Cinzel", serif;
    font-weight: 400;
    text-align: center;
    line-height: 1;
  }
  .brand__name { display: block; letter-spacing: .02em; }
  .brand__sub { display: block; letter-spacing: .55em; margin-top: 10px; }

  .card--front .brand {
    position: absolute;
    left: 50%; top: 50%;
    transform: translate(-50%, -50%);
    color: var(--white);
  }
  .card--front .brand__name { font-size: 52px; }
  .card--front .brand__sub { font-size: 17px; }

  .card--back .brand {
    position: absolute;
    left: 48px; top: 70px;
    color: var(--purple);
  }
  .card--back .brand__name { font-size: 40px; }
  .card--back .brand__sub { font-size: 14px; }

  .contact {
    position: absolute;
    left: 540px; top: 290px;
    font-family: "PT Serif", serif;
    color: var(--ink);
  }
  .contact__name {
    font-family: "Cinzel", serif;
    font-weight: 600;
    font-size: 26px;
    color: var(--purple);
    line-height: 1;
  }
  .contact__role { font-size: 19px; margin-top: 2px; }
  .contact__list { list-style: none; margin-top: 26px; font-size: 19px; line-height: 1.35; }
  .contact__label { color: var(--purple); }
</style>
</head>
<body>
  <section class="card card--front" aria-label="Card front">
    <div class="card__accent"></div>
    <div class="card__panel">
      <div class="brand">
        <span class="brand__name">LANTERN MEADOW</span>
        <span class="brand__sub">BOUTIQUE</span>
      </div>
    </div>
  </section>

  <section class="card card--back" aria-label="Card back">
    <div class="card__accent"></div>
    <div class="card__panel">
      <div class="brand">
        <span class="brand__name">LANTERN MEADOW</span>
        <span class="brand__sub">BOUTIQUE</span>
      </div>
      <div class="contact">
        <p class="contact__name">Owen Carlisle</p>
        <p class="contact__role">Founder</p>
        <ul class="contact__list">
          <li><span class="contact__label">P:</span>(123) 456-7890</li>
          <li><span class="contact__label">E:</span>info@companymail.example</li>
          <li><span class="contact__label">W:</span>www.companysite.example</li>
        </ul>
      </div>
    </div>
  </section>
</body>
</html>
```